Finiding oppertunites in Real Estate 6.15.20

size of ad 7” x 9.6”
1-I like the ad to stand out and attract people's attention.
2-you should be able to see the text of the ad clearly .. see the attachment anything in yellow is instructions.
3-the list of topics should not be the main part of the ad
4-if you decide you want a picture or vector of a person .. (you decide)
then it should be a white male about 25-30 years old wearing a solid white or blue shirt and not long hair.
5-leave 1 inch for footer
see attachment
Good luck

Target Market(s)

potential male students 25-35 years of age

Industry/Entity Type

Education

Requirements
Must have
• will stand out and people would want to see it.
should be able to read the words of ad
Nice to have
• how to make money in real estate on one line

```html
<!DOCTYPE html>
<html lang="en">
<head>
<meta charset="utf-8">
<title>Real Estate Career Course – Flyer</title>
<link rel="stylesheet" href="https://fonts.googleapis.com/css2?family=Bebas+Neue&family=Montserrat:wght@500&display=swap">
<style>
  :root {
    --stage: #c9c9c9;
    --blue: #1a93d6;
    --blue-deep: #0b84cc;
    --white: #ffffff;
    --ink: #0b0b0b;
    --photo-light: #f1f1f1;
    --photo-mid: #d9dde2;
  }
  * { margin: 0; padding: 0; box-sizing: border-box; }
  html, body { width: 1200px; height: 615px; overflow: hidden; background: var(--stage); }
  .flyer {
    position: absolute; left: 381px; top: 7px;
    width: 438px; height: 600px;
    background: var(--white); overflow: hidden;
  }
  .flyer__body {
    position: absolute; left: 0; top: 0; width: 438px; height: 565px;
    background: linear-gradient(180deg, var(--blue-deep) 0%, var(--blue) 100%);
  }
  .flyer__art { position: absolute; left: 0; top: 0; }
  .headline, .topics-title, .session-title, .session-info {
    position: absolute; font-family: "Bebas Neue", "Oswald", sans-serif;
    line-height: 1; color: var(--white); white-space: nowrap;
    transform-origin: left top;
  }
  .headline--main { left: 226px; top: 22px; font-size: 44px; }
  .headline--sub { left: 226px; top: 63px; font-size: 38px; transform: scaleX(0.98); }
  .topics-title { left: 226px; top: 121px; font-size: 34px; transform: scaleX(0.96); }
  .topics-title--dark { top: 153px; color: var(--ink); }
  .topic-list {
    position: absolute; left: 229px; top: 190px; list-style: none;
    font-family: "Montserrat", Arial, sans-serif; font-weight: 500;
    font-size: 12.2px; color: var(--white);
  }
  .topic-list li { height: 27.4px; display: flex; align-items: center; gap: 6px; }
  .topic-list svg { width: 21px; height: 21px; flex: none; }
  .intro-list {
    position: absolute; left: 25px; top: 214px; width: 180px; list-style: none;
    font-family: "Montserrat", Arial, sans-serif; font-weight: 500;
    font-size: 9.8px; line-height: 13.4px; color: var(--white);
  }
  .intro-list li { position: relative; padding-left: 10px; margin-bottom: 5.5px; white-space: nowrap; }
  .intro-list li::before {
    content: ""; position: absolute; left: 0; top: 4px;
    width: 3.5px; height: 3.5px; border-radius: 50%; background: var(--white);
  }
  .session-title {
    left: 26px; top: 336px; font-size: 32px; color: var(--ink);
    -webkit-text-stroke: 0.6px var(--white); paint-order: stroke fill;
    text-shadow: 0 0 1.5px var(--white), 0 0 1px var(--white);
    transform: scaleX(0.95);
  }
  .session-rule { position: absolute; left: 26px; top: 372px; width: 172px; height: 1.5px; background: var(--white); }
  .session-info {
    left: 27px; top: 383px; font-size: 33px; line-height: 32px;
    transform: scaleX(0.85);
  }
</style>
</head>
<body>
<article class="flyer">
  <div class="flyer__body"></div>

  <svg class="flyer__art" width="438" height="565" viewBox="0 0 438 565">
    <defs>
      <radialGradient id="photoTone" cx="0.55" cy="0.55" r="0.6">
        <stop offset="0" stop-color="var(--photo-mid)"/>
        <stop offset="1" stop-color="var(--photo-light)"/>
      </radialGradient>
    </defs>
    <circle cx="70" cy="48" r="135" fill="var(--ink)"/>
    <circle cx="68" cy="45" r="134" fill="var(--white)"/>
    <rect x="18" y="14" width="160" height="168" rx="6" fill="url(#photoTone)"
          role="img" aria-label="Photo of a young man in a white shirt pointing to the course title"/>
  </svg>

  <h1 class="headline headline--main">Real Estate</h1>
  <p class="headline headline--sub">Career Course</p>
  <h2 class="topics-title">A Partial Listing</h2>
  <h2 class="topics-title topics-title--dark">Of Topics</h2>

  <ul class="intro-list">
    <li>How to Make Money In Real<br>Estate?</li>
    <li>An investment in knowledge<br>opens up untold opportunities</li>
    <li>For those who have started or<br>would like to go into Real Estate</li>
  </ul>

  <p class="session-title">Remote Sessions</p>
  <div class="session-rule"></div>
  <p class="session-info">12 Session Course<br>Classes Starting<br>June 16</p>

  <ul class="topic-list">
    <li><svg viewBox="0 0 20 20"><circle cx="10" cy="10" r="10" fill="#fff"/><circle cx="10" cy="6.5" r="2.2" fill="#111"/><path d="M6.5 15v-4a3.5 3.5 0 0 1 7 0v4z" fill="#111"/></svg>Single-family</li>
    <li><svg viewBox="0 0 20 20"><circle cx="10" cy="10" r="10" fill="#fff"/><path d="M4.5 9.5 10 5l5.5 4.5V15h-11z" fill="#111"/><rect x="7" y="11" width="1.4" height="3" fill="#fff"/><rect x="9.3" y="11" width="1.4" height="3" fill="#fff"/><rect x="11.6" y="11" width="1.4" height="3" fill="#fff"/></svg>Multifamily</li>
    <li><svg viewBox="0 0 20 20"><circle cx="10" cy="10" r="10" fill="#fff"/><circle cx="10" cy="7" r="2.5" fill="#111"/><path d="M5.5 15a4.5 4.5 0 0 1 9 0z" fill="#111"/></svg>Management</li>
    <li><svg viewBox="0 0 20 20"><circle cx="10" cy="10" r="10" fill="#fff"/><path d="M4.5 10 10 5l5.5 5" fill="none" stroke="#111" stroke-width="1.6"/><rect x="6.5" y="10" width="7" height="5" fill="#111"/><rect x="9" y="12" width="2" height="3" fill="#fff"/></svg>Real Estate Concepts</li>
    <li><svg viewBox="0 0 20 20"><circle cx="10" cy="10" r="10" fill="#fff"/><path d="M5 10 10 5.5 15 10v5H5z" fill="none" stroke="#111" stroke-width="1.3"/><path d="M8 12.5h4M10 10v4" stroke="#111" stroke-width="1.2"/></svg>Real Estate law</li>
    <li><svg viewBox="0 0 20 20"><circle cx="10" cy="10" r="10" fill="#fff"/><circle cx="10" cy="10" r="5.5" fill="none" stroke="#111" stroke-width="1.2"/><text x="10" y="13" text-anchor="middle" font-family="Arial, sans-serif" font-size="8" font-weight="700" fill="#111">$</text></svg>Investment properties</li>
    <li><svg viewBox="0 0 20 20"><circle cx="10" cy="10" r="10" fill="#fff"/><path d="M5 10 10 6l5 4z" fill="#111"/><rect x="5" y="11" width="10" height="1.5" fill="#111"/><rect x="5" y="13.5" width="10" height="1.5" fill="#111"/></svg>Foreclosures</li>
    <li><svg viewBox="0 0 20 20"><circle cx="10" cy="10" r="10" fill="#fff"/><path d="M5.5 14.5 11 9" stroke="#111" stroke-width="2"/><rect x="10" y="5" width="5.5" height="4" rx="1" fill="#111"/></svg>Rehab</li>
    <li><svg viewBox="0 0 20 20"><circle cx="10" cy="10" r="10" fill="#fff"/><rect x="5" y="11" width="2" height="4" fill="#111"/><rect x="8.5" y="9" width="2" height="6" fill="#111"/><rect x="12" y="7" width="2" height="8" fill="#111"/><path d="M5 8.5 9 6l3 1.5 3-2.5" fill="none" stroke="#111" stroke-width="1"/></svg>Short sales</li>
    <li><svg viewBox="0 0 20 20"><circle cx="10" cy="10" r="10" fill="#fff"/><circle cx="10" cy="8" r="3" fill="none" stroke="#111" stroke-width="1.3"/><path d="M6 15l2-3M14 15l-2-3" stroke="#111" stroke-width="1.3"/></svg>Development</li>
    <li><svg viewBox="0 0 20 20"><circle cx="10" cy="10" r="10" fill="#fff"/><rect x="5.5" y="5" width="8" height="10" fill="none" stroke="#111" stroke-width="1.2"/><path d="M7.5 8h4M7.5 10.5h4M7.5 13h2" stroke="#111" stroke-width="1"/></svg>Finical modeling</li>
    <li><svg viewBox="0 0 20 20"><circle cx="10" cy="10" r="10" fill="#fff"/><path d="M4.5 9.5 10 5.5l5.5 4z" fill="#111"/><rect x="6.5" y="10" width="7" height="4.5" fill="#111"/></svg>HUD properties</li>
    <li><svg viewBox="0 0 20 20"><circle cx="10" cy="10" r="10" fill="#fff"/><circle cx="9" cy="9" r="3.5" fill="none" stroke="#111" stroke-width="1.5"/><path d="M11.5 11.5 15 15" stroke="#111" stroke-width="1.8"/></svg>Due Diligence</li>
  </ul>
</article>
</body>
</html>
```